Pilates trainer needs new website

Summary: I need a new, meaningful website in a 1-page format, but one that can be expanded if necessary. I teach in various studios and in the future also in companies. Therefore, the website should convey growth, joy, uniqueness, workout and a bit of luxury.
The website should be inviting.
Layout:
Introduction what I offer
A bit about me
Option to upload price list and timetable in PDF format
Studio address where I teach
The color scheme should be petrol, gold, and colors that match. Not too dark, please.
My current website www.movewell-brennach.de, new domain is corebalance-studio.com (I have already purchased it)
Logo file attached
I have attached a few suggestions but I am also happy to be surprised.

Target Market(s)

Pilates private and small groups,

Industry/Entity Type

Pilates teacher freelancer

Coding

Coded - Design and coding required

Number of Pages Required

1 page

Requirements
Must have
• Welcoming appearance, about me, pictures, offers, colors from the logo but don't get do dark, more fresh and a bit luxurious
Should not have
• Not too wild and going crazy with colors

```html
<!DOCTYPE html>
<html lang="en">
<head>
<meta charset="utf-8">
<title>Corebalance Studio – Maren Tollberg Pilates</title>
<link rel="stylesheet" href="https://fonts.googleapis.com/css2?family=Cinzel:wght@400&family=Poppins:wght@300;400;600;700&family=Pinyon+Script&display=swap">
<style>
:root{
  --gold:#c19a49;
  --cream:#f6efe3;
  --cream-light:#faf6ef;
  --ink:#1f1d1d;
  --text:#6d6a66;
  --leaf:#2f4a22;
  --white:#ffffff;
  --badge:#4f74a0;
}
*{box-sizing:border-box;margin:0;padding:0}
html,body{width:1200px;height:3841px;overflow:hidden;background:var(--white)}
body{position:relative;font-family:'Poppins',sans-serif;color:var(--text)}
.abs{position:absolute}
.serif{font-family:'Cinzel',serif;color:var(--ink);letter-spacing:1px;font-weight:400}
.script{font-family:'Pinyon Script',cursive;color:var(--gold);line-height:1;font-weight:400}
.btn{position:absolute;background:var(--ink);color:var(--white);font-family:'Poppins',sans-serif;font-weight:600;font-size:13px;display:flex;align-items:center;justify-content:center;gap:8px;text-transform:uppercase}

/* nav */
.nav a{position:absolute;top:88px;font-family:'Cinzel',serif;font-size:15px;color:var(--ink);text-decoration:none;letter-spacing:1px}
.nav .sep{position:absolute;top:84px;width:1px;height:24px;background:var(--ink)}
.brand{position:absolute;left:524px;top:70px;width:160px;text-align:center;display:flex;flex-direction:column;align-items:center;gap:10px}
.brand .dot{width:14px;height:14px;border-radius:50%;background:var(--ink)}
.brand span{font-family:'Cinzel',serif;font-size:17px;color:var(--ink);letter-spacing:1px}

/* hero */
.hero-band{left:526px;top:280px;width:674px;height:428px;background:var(--cream-light)}
.photo{position:absolute}
.hero-title{left:86px;top:318px;font-size:138px}
.hero-sub{left:89px;top:486px;font-size:30px;line-height:45px;letter-spacing:2px}

.leaf{position:absolute;background:radial-gradient(ellipse at 40% 40%,#4a6b33,var(--leaf) 70%)}

.motto{left:0;width:1200px;top:850px;text-align:center;font-size:21px;line-height:31px;letter-spacing:2px}

/* about */
.about-band{left:0;top:996px;width:1111px;height:550px;background:var(--cream)}
.about-frame{left:88px;top:1087px;width:377px;height:548px;background:var(--white)}
.about-card{left:540px;top:1093px;width:486px;height:356px;background:var(--white);padding:28px 58px}
.about-card h2{font-size:86px;margin-left:-4px}
.about-card h3{font-size:14px;margin-top:4px}
.about-card p{font-size:11.5px;line-height:21px;margin-top:18px;color:var(--text)}
.leaf-tip{left:346px;top:1638px;width:86px;height:80px;background:var(--cream);border-radius:0 0 50% 50%/0 0 100% 100%}

/* services */
.section-title{left:0;width:1200px;text-align:center}
.section-sub{left:0;width:1200px;text-align:center;font-size:15px}
.svc{position:absolute;top:1860px;width:325px;height:392px;background:var(--cream-light);padding:56px 54px}
.svc h3{font-family:'Cinzel',serif;font-weight:400;font-size:21px;line-height:27px;color:var(--ink);letter-spacing:1.5px}
.svc p{font-size:11.5px;line-height:19.5px;margin-top:28px}
.svc p b{color:var(--gold);font-weight:600;font-size:10px}
.svc .btn{left:54px;top:292px;width:128px;height:38px;font-size:11px}

/* testimonial */
.quote-mark{left:552px;top:2482px;width:96px;height:76px}
.quote-text{left:290px;width:620px;top:2590px;text-align:center;font-size:16px;line-height:25px;color:var(--text);font-weight:300}
.quote-name{left:0;width:1200px;top:2684px;text-align:center;color:var(--gold);font-size:12px;font-weight:600}
.dots span{position:absolute;top:2752px;width:77px;height:2px;background:#d9d6d2}
.dots span.on{background:var(--ink);height:3px}

/* promo */
.promo{left:86px;top:2847px;width:1114px;height:514px;background:var(--cream)}
.promo-clip{left:86px;top:2847px;width:1114px;height:514px;overflow:hidden}
.promo-title{left:250px;top:2940px;font-size:29px;letter-spacing:2px;line-height:36px}
.promo-save{left:250px;top:2988px;height:96px;display:flex;align-items:flex-end;gap:14px}
.promo-save .script{font-size:76px;color:var(--ink);line-height:80px}
.promo-save b{font-family:'Poppins',sans-serif;font-weight:700;font-size:96px;line-height:96px;color:var(--gold);letter-spacing:-2px}
.promo-list{left:258px;top:3102px;font-size:21px;line-height:31px;color:var(--ink);list-style:none}
.promo-list li::before{content:"";display:inline-block;width:9px;height:9px;border-radius:50%;background:var(--ink);margin:0 18px 3px 0}

/* footer */
.foot-brand{left:89px;top:3470px;width:210px;display:flex;flex-direction:column;align-items:center;gap:14px}
.foot-brand .dot{width:22px;height:22px;border-radius:50%;background:var(--ink)}
.foot-brand span{font-family:'Cinzel',serif;font-size:24px;color:var(--ink);letter-spacing:1px;text-align:center;line-height:30px}
.foot-head{left:382px;top:3448px;font-size:17px;letter-spacing:1.5px}
.info{position:absolute;font-size:12px;line-height:19px;color:var(--text)}
.info svg{position:absolute;left:-26px;top:3px}
.badge{left:963px;top:3451px;width:148px;height:179px;background:var(--badge);border-radius:4px}
.totop{left:1133px;top:3722px;width:48px;height:48px;border-radius:50%;background:var(--ink)}
.rule{left:89px;top:3745px;width:1022px;height:1px;background:#e6e3df}
.legal{top:3786px;font-family:'Cinzel',serif;font-size:12px;color:var(--ink);letter-spacing:.8px}
.social{position:absolute;top:3775px;width:38px;height:38px;border-radius:50%;background:#efeeec;display:flex;align-items:center;justify-content:center}
.social i{display:block;width:12px;height:12px;border-radius:50%;background:var(--ink)}
</style>
</head>
<body>

<nav class="nav">
  <a style="left:89px">INDIVIDUAL TRAINING</a>
  <span class="sep" style="left:316px"></span>
  <a style="left:346px">GROUP TRAINING</a>
  <a style="left:714px">TIMETABLE</a>
  <span class="sep" style="left:843px"></span>
  <a style="left:871px">ABOUT ME</a>
  <span class="sep" style="left:998px"></span>
  <a style="left:1024px">CONTACT</a>
</nav>
<div class="brand"><i class="dot"></i><span>Corebalance Studio</span></div>

<div class="abs hero-band"></div>
<div class="photo" role="img" aria-label="Photo of the trainer smiling during a Pilates exercise in the studio" style="left:671px;top:227px;width:385px;height:536px;background:linear-gradient(160deg,#d9cfc2,#b9a68e 55%,#3b4766)"></div>
<div class="abs script hero-title">Contrology</div>
<div class="abs serif hero-sub">MAREN TOLLBERG<br>PILATES STUDIO TRAINER</div>
<div class="btn" style="left:89px;top:602px;width:239px;height:41px;font-size:12px">Request an appointment now</div>

<div class="leaf" role="img" aria-label="Tropical monstera leaf decoration" style="left:0;top:730px;width:232px;height:300px;border-radius:60% 40% 55% 45%/50% 60% 40% 50%"></div>

<div class="abs serif motto">CHANGE HAPPENS THROUGH MOVEMENT<br>AND MOVEMENT HEALS</div>

<div class="abs about-band"></div>
<div class="abs leaf-tip"></div>
<div class="abs about-frame"></div>
<div class="photo" role="img" aria-label="Photo of the trainer seated on a Pilates chair in the studio" style="left:94px;top:1093px;width:365px;height:536px;background:linear-gradient(170deg,#e9e3da,#c9b48f 45%,#2d3554 75%,#e7e3de)"></div>
<div class="abs about-card">
  <h2 class="script">About</h2>
  <h3 class="serif">PILATES STUDIO AND MAT TRAINER</h3>
  <p>I discovered my love for Pilates several years ago and pretty quickly had the desire to teach this method and convince as many people as possible of its positive effects. I successfully completed my training as a Pilates mat trainer at Flowline Pilates. In order to get to know...</p>
  <div class="btn" style="left:58px;top:284px;width:114px;height:35px;font-size:11px">Read more</div>
</div>

<h2 class="abs script section-title" style="top:1718px;font-size:90px">Services</h2>
<div class="abs serif section-sub" style="top:1809px">PILATES STUDIO AND MAT TRAINER</div>

<div class="svc" style="left:88px">
  <h3>INDIVIDUAL<br>TRAINING</h3>
  <p>To get to know the Pilates method or because you don't have time to take part in group classes? Are you pursuing a specific training goal, have physical limitations or would you like to try Pilates for the first time as a beginner. <b>MORE</b></p>
  <div class="btn"><svg width="16" height="16" viewBox="0 0 16 16" fill="none" stroke="#fff" stroke-width="1.6"><path d="M8 2v8M4.5 6.5 8 10l3.5-3.5M2 11v3h12v-3"/></svg>Price list</div>
</div>
<div class="photo" role="img" aria-label="Photo of the trainer exercising on a Pilates reformer" style="left:437px;top:1860px;width:325px;height:392px;background:linear-gradient(180deg,#d9cbb3,#a89a86 50%,#3d4360)"></div>
<div class="svc" style="left:786px">
  <h3>GROUP<br>TRAINING</h3>
  <p>Through consistent, correctly guided practice, you can achieve a fundamental improvement in your movement habits. The key is to provide a successful, pain-free movement experience that prevents long-term poor posture. <b>MORE</b></p>
  <div class="btn"><svg width="16" height="16" viewBox="0 0 16 16" fill="none" stroke="#fff" stroke-width="1.6"><path d="M8 2v8M4.5 6.5 8 10l3.5-3.5M2 11v3h12v-3"/></svg>Price list</div>
</div>

<div class="leaf" role="img" aria-label="Tropical leaf decoration" style="left:0;top:2210px;width:125px;height:260px;border-radius:0 70% 30% 0/0 50% 50% 0"></div>

<h2 class="abs script section-title" style="top:2330px;font-size:90px">Testimonial</h2>
<div class="abs serif section-sub" style="top:2430px">THIS IS WHAT CUSTOMERS SAY ABOUT ME</div>
<svg class="abs quote-mark" viewBox="0 0 96 76"><path fill="#1f1d1d" d="M0 76V40C0 16 10 4 34 0l3 10C24 14 18 22 18 34h22v42zM56 76V40C56 16 66 4 90 0l3 10C80 14 74 22 74 34h22v42z"/></svg>
<p class="abs quote-text">Clara is a very good Pilates trainer. She also takes an enormous amount of time for each individual in group training sessions. It makes a lot of fun. That's why I booked the 10 ticket straight away.</p>
<div class="abs quote-name">CLARA B.</div>
<div class="dots"><span style="left:475px"></span><span class="on" style="left:562px"></span><span style="left:649px"></span></div>

<div class="leaf" role="img" aria-label="Fan palm leaf decoration" style="left:900px;top:2580px;width:300px;height:260px;border-radius:100% 0 0 30%/100% 0 0 40%;background:radial-gradient(ellipse at 100% 60%,#3e5a2c,#6f8a5c 60%,rgba(255,255,255,0) 75%)"></div>

<div class="abs promo"></div>
<div class="abs promo-clip"><div class="abs" style="left:585px;top:252px;width:504px;height:504px;border-radius:50%;background:var(--white)"></div></div>
<div class="photo" role="img" aria-label="Gold line illustration of a woman in a seated Pilates stretch" style="left:740px;top:2892px;width:380px;height:469px;background:linear-gradient(160deg,rgba(193,154,73,.35),rgba(193,154,73,.12))"></div>
<div class="photo" role="img" aria-label="Ginkgo flower sketch decoration" style="left:0;top:2985px;width:190px;height:230px;border-radius:50%;background:radial-gradient(circle,rgba(214,190,188,.6),rgba(246,239,227,0) 70%)"></div>
<div class="abs serif promo-title">KICKSTART YOUR 2018!</div>
<div class="abs promo-save"><span class="script">Save</span><b>20%</b></div>
<ul class="abs promo-list">
  <li>On Bespoke</li><li>1-1 Personal Training</li><li>Sessions Throughout</li><li>January</li>
</ul>
<div class="btn" style="left:255px;top:3239px;width:149px;height:46px">View offers</div>

<div class="abs foot-brand"><i class="dot"></i><span>Corebalance<br>Studio</span></div>
<div class="abs serif foot-head">DID I WAKE YOUR INTEREST?</div>

<div class="info" style="left:416px;top:3490px">
  <svg width="14" height="18" viewBox="0 0 14 18"><path fill="#c19a49" d="M7 0a7 7 0 0 0-7 7c0 5 7 11 7 11s7-6 7-11a7 7 0 0 0-7-7zm0 9.5A2.5 2.5 0 1 1 7 4.5a2.5 2.5 0 0 1 0 5z"/></svg>
  Studio address Lindenau:<br>Birkenweg 7<br>83001 Lindenau<br>Entrance around the corner 2nd floor
</div>
<div class="info" style="left:416px;top:3590px">
  <svg width="14" height="18" viewBox="0 0 14 18"><path fill="#c19a49" d="M7 0a7 7 0 0 0-7 7c0 5 7 11 7 11s7-6 7-11a7 7 0 0 0-7-7zm0 9.5A2.5 2.5 0 1 1 7 4.5a2.5 2.5 0 0 1 0 5z"/></svg>
  Studio address Mühlbach:<br>Marktstraße 18<br>82010 Mühlbach
</div>
<div class="info" style="left:729px;top:3490px">
  <svg width="16" height="14" viewBox="0 0 16 14"><path fill="#c19a49" d="M0 2h16v10H0zm1.5 1.2L8 8l6.5-4.8V3L8 7 1.5 3z"/></svg>
  Write me an email<br>info@movewell-brennach.de
</div>
<div class="info" style="left:729px;top:3550px">
  <svg width="15" height="15" viewBox="0 0 15 15"><path fill="#c19a49" d="M3 0l3 3-1.6 2.2a9 9 0 0 0 5.4 5.4L12 9l3 3-2 2.5C6.5 14 1 8.5.5 2z"/></svg>
  Call me<br>+49 170 5550123
</div>
<div class="info" style="left:729px;top:3609px">
  <svg width="14" height="18" viewBox="0 0 14 18"><path fill="#c19a49" d="M7 0a7 7 0 0 0-7 7c0 5 7 11 7 11s7-6 7-11a7 7 0 0 0-7-7zm0 9.5A2.5 2.5 0 1 1 7 4.5a2.5 2.5 0 0 1 0 5z"/></svg>
  Am Seeufer 12<br>83020 Brennach
</div>

<div class="abs badge" role="img" aria-label="Association membership badge"></div>

<div class="abs totop"><svg width="48" height="48" viewBox="0 0 48 48"><path d="M20 26l4-4 4 4" stroke="#fff" stroke-width="1.6" fill="none"/></svg></div>
<div class="abs rule"></div>
<div class="abs legal" style="left:89px">© COPYRIGHT MAREN TOLLBERG</div>
<div class="abs legal" style="left:462px;word-spacing:2px">PILATES GLOSSARY &nbsp;&nbsp;|&nbsp;&nbsp; PRIVACY POLICY &nbsp;&nbsp;|&nbsp;&nbsp; IMPRINT</div>
<a class="social" style="left:972px" aria-label="Social profile"><i></i></a>
<a class="social" style="left:1020px" aria-label="Social profile"><i></i></a>
<a class="social" style="left:1071px" aria-label="Messenger contact"><i></i></a>

</body>
</html>
```